Birchline Cabinets & Countertops Business Cards

We need a new business card design. Pixel Harbor did a great job on our logo design so let's get that business card done. We build custom kitchen and bath cabinets. We also do cabinets for mud rooms, closets, living rooms, bars, etc.
We would like to include a QR code somewhere in addition to our Name, Position, Email, Phone, Cell and Web Site. On the back of the card, we want to use that space to include all the various types of projects we design for. Also I am not sure it would like good or not, but a faint watermark kitchen CAD layout, etc might look cool.
To see the categories or project types we do, visit our website at https://birchlinecabinetsandcounters.example
Just be creative and give us what you got!
Contact Information for Business Card
Name, Position, Phone, Cell Phone, Email, Website, QR Code

```html
<!DOCTYPE html>
<html lang="en">
<head>
<meta charset="utf-8">
<title>Birchline Cabinets &amp; Countertops – Business Card</title>
<link href="https://fonts.googleapis.com/css2?family=Jost:wght@400;500&display=swap" rel="stylesheet">
<style>
  :root {
    --backdrop: #707070;
    --card: #ffffff;
    --navy: #1f3f73;
    --gold: #c9b074;
    --ink: #1a1a1a;
    --rule: #c4c4c4;
  }
  * { margin: 0; padding: 0; box-sizing: border-box; }
  html, body {
    width: 1200px; height: 1200px; overflow: hidden;
    background: var(--backdrop);
    font-family: "Jost", "Futura", sans-serif;
  }
  .canvas { position: relative; width: 1200px; height: 1200px; }
  .card {
    position: absolute; left: 150px; width: 898px; height: 525px;
    background: var(--card);
    box-shadow: 0 6px 14px rgba(0,0,0,.35);
  }
  .card--front { top: 55px; }
  .card--back { top: 620px; }

  .accent-band {
    position: absolute; left: 44px; top: 0; width: 46px; height: 100%;
    background: var(--gold);
  }

  .person { position: absolute; left: 101px; top: 56px; color: var(--navy); }
  .person-name { font-size: 28px; font-weight: 500; letter-spacing: .5px; line-height: 34px; }
  .person-role { font-size: 16px; letter-spacing: 2.5px; text-transform: uppercase; line-height: 26px; }

  .contact-icons { position: absolute; left: 56px; top: 160px; width: 22px; }
  .contact-icons svg { position: absolute; left: 0; width: 22px; height: 22px; fill: var(--ink); }
  .icon-rule { position: absolute; left: 1px; width: 20px; height: 1px; background: var(--ink); opacity: .6; }

  .contact-list {
    position: absolute; left: 101px; top: 150px;
    color: var(--navy); font-size: 22px; line-height: 41px; list-style: none;
    letter-spacing: .2px;
  }
  .address {
    position: absolute; left: 101px; top: 340px;
    color: var(--navy); font-size: 22px; line-height: 41px; font-style: normal;
  }

  .brand-front {
    position: absolute; left: 560px; top: 180px; width: 310px;
    display: flex; align-items: center; gap: 14px;
  }
  .brand-dot { flex: none; width: 34px; height: 34px; border-radius: 50%; background: var(--navy); }
  .brand-name {
    color: var(--navy); font-weight: 400; text-transform: uppercase;
    letter-spacing: 3px; font-size: 22px; line-height: 1.35;
  }

  .qr-slot {
    position: absolute; left: 744px; top: 330px; width: 110px; height: 110px;
    border: 3px solid var(--navy); background: #eef1f6;
  }

  .brand-back {
    position: absolute; left: 0; top: 120px; width: 100%;
    display: flex; flex-direction: column; align-items: center; gap: 40px;
  }
  .brand-back .brand-dot { width: 70px; height: 70px; }
  .brand-back .brand-name {
    font-size: 40px; letter-spacing: 6px; text-align: center; line-height: 1.3;
  }

  .project-types {
    position: absolute; left: 120px; right: 120px; top: 410px;
    display: flex; align-items: center; gap: 18px;
    color: var(--navy); font-size: 16px; letter-spacing: 3px; text-transform: uppercase;
  }
  .project-types::before, .project-types::after {
    content: ""; flex: 1; height: 1px; background: var(--rule);
  }
  .project-types ul { list-style: none; display: flex; gap: 14px; white-space: nowrap; }
  .project-types li + li::before { content: "·"; margin-right: 14px; color: var(--gold); }
</style>
</head>
<body>
<main class="canvas">

  <section class="card card--front" aria-label="Card front">
    <div class="accent-band"></div>

    <div class="person">
      <p class="person-name">Jordan Avery</p>
      <p class="person-role">Owner &amp; Lead Designer</p>
    </div>

    <div class="contact-icons" aria-hidden="true">
      <svg style="top:0" viewBox="0 0 24 24"><path d="M6.6 10.8a15.1 15.1 0 0 0 6.6 6.6l2.2-2.2a1 1 0 0 1 1-.25 11.4 11.4 0 0 0 3.6.57 1 1 0 0 1 1 1V20a1 1 0 0 1-1 1A17 17 0 0 1 3 4a1 1 0 0 1 1-1h3.5a1 1 0 0 1 1 1c0 1.25.2 2.45.57 3.57a1 1 0 0 1-.25 1z"/></svg>
      <span class="icon-rule" style="top:32px"></span>
      <svg style="top:41px" viewBox="0 0 24 24"><path d="M7 1h10a2 2 0 0 1 2 2v18a2 2 0 0 1-2 2H7a2 2 0 0 1-2-2V3a2 2 0 0 1 2-2zm0 3v14h10V4zm5 15.5a1.2 1.2 0 1 0 0 2.4 1.2 1.2 0 0 0 0-2.4z"/></svg>
      <span class="icon-rule" style="top:73px"></span>
      <svg style="top:82px" viewBox="0 0 24 24"><path d="M3 5h18a1 1 0 0 1 1 1v12a1 1 0 0 1-1 1H3a1 1 0 0 1-1-1V6a1 1 0 0 1 1-1zm9 7.2L20 7H4z"/></svg>
      <span class="icon-rule" style="top:114px"></span>
      <svg style="top:123px" viewBox="0 0 24 24"><path d="M12 2a10 10 0 1 0 0 20 10 10 0 0 0 0-20zm6.9 6h-3a15 15 0 0 0-1.3-3.9A8 8 0 0 1 18.9 8zM12 4.1c.8 1.1 1.5 2.4 1.9 3.9h-3.8c.4-1.5 1.1-2.8 1.9-3.9zM4.3 14a8 8 0 0 1 0-4h3.4a16 16 0 0 0 0 4zm.8 2h3a15 15 0 0 0 1.3 3.9A8 8 0 0 1 5.1 16zm3-8h-3a8 8 0 0 1 4.3-3.9A15 15 0 0 0 8.1 8zM12 19.9c-.8-1.1-1.5-2.4-1.9-3.9h3.8c-.4 1.5-1.1 2.8-1.9 3.9zm2.3-5.9H9.7a14 14 0 0 1 0-4h4.6a14 14 0 0 1 0 4zm.3 5.9a15 15 0 0 0 1.3-3.9h3a8 8 0 0 1-4.3 3.9zm1.7-5.9a16 16 0 0 0 0-4h3.4a8 8 0 0 1 0 4z"/></svg>
      <svg style="top:190px" viewBox="0 0 24 24"><path d="M12 2a7 7 0 0 0-7 7c0 5.2 7 13 7 13s7-7.8 7-13a7 7 0 0 0-7-7zm0 9.5A2.5 2.5 0 1 1 12 6.5a2.5 2.5 0 0 1 0 5z"/></svg>
    </div>

    <ul class="contact-list">
      <li>(850) 555-0147</li>
      <li>(850) 555-0182</li>
      <li>info@birchlinecabinetsandcounters.example</li>
      <li>birchlinecabinetsandcounters.example</li>
    </ul>

    <address class="address">
      4410 Harborlight Pkwy<br>
      Suite 210-B<br>
      Seabrook Cove, FL 32999
    </address>

    <div class="brand-front">
      <span class="brand-dot" aria-hidden="true"></span>
      <span class="brand-name">Birchline Cabinets &amp; Countertops</span>
    </div>

    <div class="qr-slot" role="img" aria-label="QR code linking to the company website"></div>
  </section>

  <section class="card card--back" aria-label="Card back">
    <div class="brand-back">
      <span class="brand-dot" aria-hidden="true"></span>
      <h1 class="brand-name">Birchline Cabinets<br>&amp; Countertops</h1>
    </div>

    <div class="project-types">
      <ul>
        <li>Kitchens</li>
        <li>Baths</li>
        <li>Mud Rooms</li>
        <li>Closets</li>
        <li>Living Rooms</li>
        <li>Bars</li>
      </ul>
    </div>
  </section>

</main>
</body>
</html>
```